VarloPeak

Need a 6 page template designed in Layered PSD for a house cleaning company.

Target Market(s)

People who are selling their homes and need house cleaning

Industry/Entity Type

House cleaning

Number of Pages Required

5+ page

Font styles to use
Sans Serif

Requirements
Must have
• Please see the zip file included with the brief. It has a document with detailed instructions.

```html
<!DOCTYPE html>
<html lang="en">
<head>
<meta charset="utf-8">
<title>VarloPeak – Barrie Area Deep Cleaning</title>
<link href="https://fonts.googleapis.com/css2?family=Montserrat:wght@400;500;600;700&display=swap" rel="stylesheet">
<style>
:root{
  --blue:#1f4a96;
  --green:#5cb531;
  --ink:#222;
  --text:#444;
  --soft:#f6f6f6;
  --dark:#2c3034;
  --white:#fff;
}
*{box-sizing:border-box;margin:0;padding:0}
html,body{width:1200px;height:4587px;overflow:hidden}
body{font-family:'Montserrat',sans-serif;color:var(--text);background:var(--white);position:relative}
.abs{position:absolute}
p{font-size:13.5px;line-height:1.55}
.green{color:var(--green)}
.blue{color:var(--blue)}

/* header */
.site-header{position:absolute;top:0;left:0;width:1200px;height:107px;background:var(--white)}
.brand{position:absolute;left:89px;top:30px;display:flex;align-items:center;gap:10px;font-size:34px;font-weight:700;color:var(--blue)}
.brand .dot{width:16px;height:16px;border-radius:50%;background:var(--green)}
.contact-line{position:absolute;right:89px;top:20px;display:flex;gap:30px;font-size:13px;font-weight:600;color:var(--ink)}
.contact-line span{display:flex;align-items:center;gap:7px}
.nav{position:absolute;left:400px;top:62px;display:flex;gap:37px;font-size:13.5px;font-weight:600;color:var(--ink)}
.nav .active{color:var(--green);text-decoration:underline}
.quote-btn{position:absolute;left:913px;top:53px;width:199px;height:37px;background:var(--blue);color:var(--white);font-size:12.5px;font-weight:600;display:flex;align-items:center;justify-content:center;border-radius:3px}

/* hero */
.hero{position:absolute;top:107px;left:0;width:1200px;height:480px;background:linear-gradient(100deg,#5e6b71 0%,#8a9398 35%,#c9c4bb 60%,#e4ded2 100%)}
.hero-text{position:absolute;left:86px;top:162px;color:var(--white)}
.hero-text .lead{font-size:26px;line-height:1.4;font-weight:500}
.hero-text h1{font-size:33px;line-height:1.25;font-weight:700;margin-top:4px}
.dots{position:absolute;left:565px;top:444px;display:flex;gap:10px}
.dots i{width:17px;height:17px;border:2px solid var(--white);border-radius:50%}
.dots i.on{background:rgba(255,255,255,.5)}

/* welcome */
.welcome{position:absolute;top:587px;left:0;width:1200px;height:380px}
.welcome-copy{position:absolute;left:89px;top:75px;width:610px}
.welcome-copy h2{font-size:17px;line-height:1.4;color:var(--green);font-weight:700;margin-bottom:20px}
.welcome-copy p{margin-bottom:22px}
.welcome-mark{position:absolute;left:760px;top:160px;display:flex;align-items:center;gap:14px;font-size:64px;font-weight:700;color:var(--blue)}
.welcome-mark .dot{width:26px;height:26px;border-radius:50%;background:var(--green)}

/* services */
.services{position:absolute;top:960px;left:0;width:1200px;height:760px;background:var(--soft)}
.services .wave{position:absolute;top:-1px;left:0}
.ring{position:absolute;border-radius:50%;border:22px solid #e3efd9}
.section-title{text-align:center;font-weight:700;font-size:33px;line-height:1.25}
.tabs{position:absolute;top:250px;left:0;width:1200px;display:flex;justify-content:center;gap:22px;font-size:15px;font-weight:500;color:var(--blue)}
.tabs .sep{color:#999}
.block-copy h3{font-size:22px;font-weight:600;color:var(--green);margin-bottom:6px}
.block-copy h4{font-size:14.5px;font-weight:600;color:var(--ink);margin-bottom:18px}
.block-copy p{margin-bottom:16px}
.photo{position:absolute;border:3px solid var(--white);box-shadow:0 0 0 1px #ddd}

/* move-in */
.movein{position:absolute;top:1670px;left:0;width:1200px;height:810px}
.movein .block-copy h3{color:var(--green)}
.movein .block-copy h4,.movein .block-copy p{color:var(--white)}
.realtor{position:absolute;left:559px;top:413px;width:553px;height:277px;background:var(--white);padding:20px 24px}
.realtor h5{font-size:14.5px;font-weight:600;color:var(--ink);margin-bottom:12px}
.realtor p{margin-bottom:10px}
.btn-green{display:inline-block;background:var(--green);color:var(--white);font-size:12.5px;font-weight:700;padding:10px 22px;margin:6px 0 14px;border-radius:2px}

/* move-out */
.moveout{position:absolute;top:2480px;left:0;width:1200px;height:760px}
.sub{font-size:14.5px;font-weight:600;color:var(--ink);margin:12px 0 4px}

/* only */
.only{position:absolute;top:3240px;left:0;width:1200px;height:340px}
.only h2{font-size:32px;font-weight:600;color:var(--ink);line-height:1.28;text-align:center;margin-top:70px}
.only p{text-align:center;width:800px;margin:28px auto 0;font-size:13.5px;line-height:1.75}

/* blogs */
.blogs{position:absolute;top:3560px;left:0;width:1200px;height:680px}
.blogs h2{position:absolute;top:143px;width:1200px;text-align:center;font-size:32px;font-weight:700;color:var(--blue)}
.card{position:absolute;top:205px;width:324px}
.card .img{height:202px;border:3px solid var(--white);box-shadow:0 0 0 1px #ccc;background:linear-gradient(120deg,#8c9196,#d9d3c7 60%,#c9a45a)}
.card .date{font-size:13.5px;font-weight:700;color:var(--green);margin-top:8px}
.card p{margin-top:4px;color:var(--green);font-size:13.5px}
.card .more{font-size:12.5px;color:var(--green);margin-top:12px}
.view-all{position:absolute;top:550px;left:544px;width:113px;height:35px;background:var(--blue);color:var(--white);font-size:12.5px;font-weight:700;display:flex;align-items:center;justify-content:center;border-radius:2px}

/* footer */
.site-footer{position:absolute;top:4237px;left:0;width:1200px;height:311px;background:var(--dark);color:#e6e6e6}
.footer-brand{position:absolute;left:89px;top:170px;display:flex;align-items:center;gap:10px;font-size:38px;font-weight:700;color:var(--blue)}
.footer-brand .dot{width:16px;height:16px;border-radius:50%;background:var(--green)}
.fcol{position:absolute;top:76px;font-size:13.5px;line-height:1.95}
.fcol h6{font-size:15px;font-weight:700;color:var(--green);margin-bottom:6px}
.fcol a{display:block;color:#e6e6e6;text-decoration:none}
.fcol a.current{color:var(--green);text-decoration:underline}
.areas{display:flex;gap:28px}
.areas div{width:95px}
.to-top{position:absolute;left:1128px;top:244px;width:40px;height:40px;border-radius:50%;background:var(--green);display:flex;align-items:center;justify-content:center}
.copyright{position:absolute;top:4548px;left:0;width:1200px;height:39px;background:var(--blue);color:var(--white);font-size:13px;display:flex;align-items:center;justify-content:center}
</style>
</head>
<body>

<header class="site-header">
  <div class="brand"><span class="dot"></span>VarloPeak</div>
  <div class="contact-line">
    <span><svg width="13" height="13" viewBox="0 0 24 24"><path fill="#5cb531" d="M6.6 10.8a15 15 0 0 0 6.6 6.6l2.2-2.2a1 1 0 0 1 1-.25 11.4 11.4 0 0 0 3.6.57 1 1 0 0 1 1 1V20a1 1 0 0 1-1 1A17 17 0 0 1 3 4a1 1 0 0 1 1-1h3.5a1 1 0 0 1 1 1c0 1.25.2 2.45.57 3.6a1 1 0 0 1-.25 1z"/></svg>555-014-2287</span>
    <span><svg width="14" height="11" viewBox="0 0 24 18"><rect width="24" height="18" rx="2" fill="#5cb531"/><path d="M1 1l11 9 11-9" stroke="#fff" stroke-width="2" fill="none"/></svg>info.varlopeak.com</span>
  </div>
  <nav class="nav"><span class="active">HOME</span><span>ABOUT US</span><span>SERVICES</span><span>BLOGS</span><span>CONTACT US</span></nav>
  <div class="quote-btn">EASY ONLINE QUOTES</div>
</header>

<section class="hero" role="img" aria-label="Cleaner in yellow gloves wiping a living room table with a spray bottle">
  <div class="hero-text">
    <div class="lead">The Only Barrie Area Cleaning<br>Service That Specializes in</div>
    <h1>Deep Pre-Sale, Move-In, &amp;<br>Move-Out House Cleanings</h1>
  </div>
  <div class="dots"><i></i><i class="on"></i><i></i></div>
</section>

<section class="welcome">
  <div class="welcome-copy">
    <h2>Welcome to the only Barrie area cleaning service specializing in deep move-in, move-out, and pre-sale house cleanings.</h2>
    <p>Moving in or out of a home can be daunting with so much to organize and prepare. Cleaning is often the last thing on your mind, but it's essential to sell your home quickly and to have a clean, hygienic environment in your new home for you and your family when you move in.</p>
    <p>Whether you're moving in or out of a Barrie area home, apartment, or rental property, our Barrie area Pre-Sale, Move-In, and Move-Out Deep Cleaning Services are the perfect solution for you.</p>
  </div>
  <div class="welcome-mark"><span class="dot"></span>VarloPeak</div>
</section>

<section class="services">
  <svg class="wave" width="1200" height="60" viewBox="0 0 1200 60"><path d="M0 0H1200V20Q600 80 0 0Z" fill="#fff"/></svg>
  <div class="ring" style="left:-10px;top:60px;width:260px;height:260px"></div>
  <div class="section-title abs" style="top:145px;width:1200px"><span class="green">CLEANING SERVICES</span><br><span class="blue">WE OFFER</span></div>
  <div class="tabs"><span class="green">Pre-Sale Cleaning</span><span class="sep">|</span><span>Move-In Cleaning</span><span class="sep">|</span><span>Move-Out Cleaning</span><span class="sep">|</span><span>Junk Removal</span></div>
  <div class="block-copy abs" style="left:89px;top:350px;width:554px">
    <h3>Pre-Sale Cleanings:</h3>
    <h4>Are You Putting Your Barrie Area Home Up for Sale?</h4>
    <p>First impressions matter, and a clean and fresh home can make a huge difference. At VarloPeak.com, we specialize in deep cleaning services that will get your home in tip-top shape for potential buyers.</p>
    <p>Not only will a move-out deep cleaning make your home more attractive to potential buyers, but it can also increase its value. A well-maintained home is a valuable asset that can command a higher price on the Barrie area market.</p>
    <p>Let us take the stress out of preparing your home for sale. Our Barrie area pre-sale deep cleaning services are tailored to your needs and can be scheduled at a time that works for you. We guarantee your satisfaction and promise to leave your home sparkling clean.</p>
  </div>
  <div class="photo" role="img" aria-label="Cleaner in pink gloves scrubbing a floor with a brush and spray bottle" style="left:714px;top:328px;width:396px;height:330px;background:linear-gradient(135deg,#d8c9a3,#b0a7a9 50%,#5f7ea0)"></div>
</section>

<section class="movein">
  <svg class="abs" style="top:0;left:0" width="1200" height="810" viewBox="0 0 1200 810"><path d="M0 0Q600 140 1200 70V740Q600 690 0 810Z" fill="#1f4a96"/></svg>
  <div class="photo" role="img" aria-label="Cleaner vacuuming a tiled hallway with a wet vacuum" style="left:89px;top:155px;width:398px;height:533px;background:linear-gradient(160deg,#c9cdd0,#9a9a92 50%,#6d6a5e)"></div>
  <div class="block-copy abs" style="left:559px;top:148px;width:553px">
    <h3>Move-In Cleanings:</h3>
    <h4>Take the Stress Out of Your Move &amp; Have Your Home Sparkling Clean Before You Move In</h4>
    <p>Moving doesn't have to be a stressful experience. Let us take the hassle out of your move and ensure your new Barrie home is clean, fresh, and ready for you to settle in.</p>
    <p>Our Barrie area move-in deep cleaning Service is designed so that you can start your new chapter with a spotless and hygienic environment. Our experienced and skilled cleaners will work diligently to ensure that every nook and cranny of your new Barrie home is perfectly cleaned.</p>
  </div>
  <div class="realtor">
    <h5>Attention Realtors</h5>
    <p>As a Barrie area realtor, you know that buying or selling a home can be stressful for your clients.</p>
    <p>Here at VarloPeak.com, we want to help make that process as smooth as possible.</p>
    <span class="btn-green">MORE INFO</span>
    <p>Let us take the hassle out of your client's move and ensure their Barrie home is deep-cleaned, fresh, and ready.</p>
  </div>
</section>

<section class="moveout">
  <div class="block-copy abs" style="left:89px;top:72px;width:554px">
    <h3>Move-Out Cleanings:</h3>
    <h4 style="margin-bottom:6px">Cleaned &amp; Ready for The Next Occupants</h4>
    <p>Looking for a professional move-out cleaning service to ensure that your property is left sparkling clean and ready for the next occupants? Look no further than our expert team of cleaning professionals!</p>
    <p style="margin-top:10px">At VarloPeak.com, we provide move-out cleaning services to homeowners and tenants throughout the Barrie area. Our team of experienced and fully trained cleaners will work tirelessly to ensure your property is left in pristine condition when you move out so that you can focus on your move without any added stress.</p>
    <div class="sub">Move-Out Cleaning for Homeowners:</div>
    <p>Move-out cleaning for Barrie area homeowners is a deep cleaning service typically performed when the homeowner prepares to move out. The purpose of move-out cleaning is to leave the property in a sparkling clean condition, ready for the next occupants to move in or for the final inspection by the new homeowner.</p>
  </div>
  <div class="photo" role="img" aria-label="Cleaner in mask and blue gloves wiping a kitchen counter" style="left:714px;top:80px;width:396px;height:338px;background:linear-gradient(135deg,#e7e2da,#c8c2b8 55%,#7f93a7)"></div>
  <div class="abs" style="left:89px;top:477px;width:1022px">
    <div class="sub">Move-Out Cleaning for Renters:</div>
    <p>Are you moving out of your Barrie area rental property soon and need to ensure that the property is left clean and in pristine condition to get your security deposit back? Don't let the stress of move-out cleaning get in the way of getting your security deposit back. Contact us today to schedule your move-out cleaning service, and let us help you leave your rental in pristine condition when you move out.</p>
    <div class="sub" style="margin-top:18px">Move Out Cleaning for Landlords &amp; Property Managers:</div>
    <p>Move-out cleaning for Barrie area landlords &amp; property managers is a deep cleaning service typically performed when a tenant vacates the rental property.<br>This deep cleaning is critical in ensuring that rental properties are in good condition, ready for new tenants, and preventing any delays in the turnover process.</p>
  </div>
</section>

<section class="only">
  <div class="ring" style="left:1040px;top:185px;width:200px;height:200px"></div>
  <h2>THE ONLY BARRIE AREA CLEANING SERVICE<br>THAT SPECIALIZES IN DEEP PRE-SALE, MOVE-IN<br>&amp; MOVE-OUT HOUSE CLEANINGS</h2>
  <p>Whether you're moving into or out of a Barrie area home, apartment, or rental property, our Barrie area Pre-Sale, Move-In, and Move-Out Deep Cleaning Services are the perfect solution for you.<br>Contact us today to schedule an appointment, and let us take care of the daunting task of having your home deep cleaned so that you can enjoy your new Barrie area home from day one.</p>
</section>

<section class="blogs">
  <svg class="abs" style="top:0;left:0" width="1200" height="60" viewBox="0 0 1200 60"><path d="M0 18Q600 -30 1200 18V60Q600 10 0 60Z" fill="#5cb531"/></svg>
  <h2>BLOGS</h2>
  <article class="card" style="left:88px"><div class="img" role="img" aria-label="Cleaner wiping a living room table"></div><div class="date">26/02/2023</div><p>Lorem Ipsum is simply dummy text of the printing and typesetting industry.</p><div class="more">Read More...</div></article>
  <article class="card" style="left:438px"><div class="img" role="img" aria-label="Two cleaners mopping and dusting an office" style="background:linear-gradient(120deg,#d8d5cf,#9b9a96 60%,#3f4347)"></div><div class="date">26/02/2023</div><p>Lorem Ipsum is simply dummy text of the printing and typesetting industry.</p><div class="more">Read More...</div></article>
  <article class="card" style="left:787px"><div class="img" role="img" aria-label="Cleaner wiping a living room table"></div><div class="date">26/02/2023</div><p>Lorem Ipsum is simply dummy text of the printing and typesetting industry.</p><div class="more" style="text-decoration:underline">Read More...</div></article>
  <div class="view-all">VIEW ALL</div>
</section>

<footer class="site-footer">
  <div class="footer-brand" style="top:150px"><span class="dot"></span>VarloPeak</div>
  <div class="fcol" style="left:353px"><h6>QUICK LINK</h6><a class="current">Home</a><a>About Us</a><a>Services</a><a>Blogs</a><a>Contact Us</a></div>
  <div class="fcol" style="left:513px;width:200px"><h6>AVAILABILITY</h6>Open 7 Days a Week<br>(Monday-Sunday)<br>Hours 8:00 am – 9:00 pm<br>Evenings &amp; Weekends (Yes)<br>Short Notice (Yes)</div>
  <div class="fcol" style="left:743px"><h6>AREAS WE SERVICE</h6>
    <div class="areas">
      <div>Barrie<br>Innisfil<br>Springwater<br>Minesing<br>Orillia<br>Wasaga</div>
      <div>Midland<br>Angus<br>Collingwood<br>New Lowell<br>Oro-Medonte<br>Shanty Bay</div>
      <div style="width:140px">Coldwater<br>Stayner<br>Creemore<br>Alliston<br>And everywhere in between</div>
    </div>
  </div>
  <div class="to-top"><svg width="16" height="16" viewBox="0 0 16 16"><path d="M8 14V2M3 7l5-5 5 5" stroke="#fff" stroke-width="2" fill="none"/></svg></div>
</footer>
<div class="copyright">Copyright © VarloPeak. All Rights Reserved</div>

</body>
</html>
```